high-impact, conversion-focused website redesign for the government sector

Objective: To design and develop a high-impact, conversion-focused digital platform that solidifies Harrowfield Bright Associates (HBA) as the leading communications and strategy firm for government, defense, and industrial clients. The site must project authority, innovation, and sophisticated precision. See the creative breif for more information

Target Market(s)

Government contractors

Industry/Entity Type

Government, defense, industrials

Coding

Coded - Design and coding required

Number of Pages Required

5+ page

Font styles to use
Other font styles liked:
• See the current website

Requirements
Must have
• See design brief
Nice to have
• See design brief
Should not have
• See design brief

```html
<!DOCTYPE html>
<html lang="en">
<head>
<meta charset="utf-8">
<title>Harrowfield Bright Associates — Results</title>
<link rel="stylesheet" href="https://fonts.googleapis.com/css2?family=Rajdhani:wght@300;400;700&family=Work+Sans:wght@400;500&display=swap">
<style>
  :root {
    --navy: #0f2c43;
    --white: #ffffff;
    --ink: #0f2c43;
    --accent: #2b8ef0;
    --muted: #dfe6ee;
    --divider: #e6e8eb;
    --topline: #3a3a3a;
    --quote: #1f4f7c;
  }
  * { margin: 0; padding: 0; box-sizing: border-box; }
  html, body { width: 1200px; height: 575px; overflow: hidden; background: var(--white); }
  body { position: relative; font-family: "Work Sans", sans-serif; }

  .site-header {
    position: absolute; top: 0; left: 0; width: 1200px; height: 35px;
    border-top: 1px solid var(--topline);
    border-bottom: 1px solid var(--divider);
    background: var(--white);
  }
  .nav-link {
    position: absolute; top: 12px; font-size: 9px; font-weight: 500;
    color: var(--ink); text-decoration: none; letter-spacing: 0.2px;
  }
  .brand {
    position: absolute; top: 14px; left: 600px; transform: translateX(-50%);
    font-size: 5px; font-weight: 500; color: var(--ink); white-space: nowrap;
    display: flex; align-items: center; gap: 2px;
  }
  .brand-dot { width: 3px; height: 3px; border-radius: 50%; background: var(--accent); }

  .results {
    position: absolute; top: 87px; left: 0; width: 1200px; height: 488px;
    background: var(--navy); color: var(--white); text-align: center;
  }
  .results-title {
    position: absolute; top: 82px; left: 0; width: 100%;
    font-family: "Rajdhani", sans-serif; font-weight: 700; font-size: 37px; line-height: 1;
  }
  .results-intro {
    position: absolute; top: 145px; left: 360px; width: 480px;
    font-size: 12.6px; line-height: 18.2px; letter-spacing: 0.35px; color: var(--white);
  }
  .stat { position: absolute; top: 248px; width: 230px; margin-left: -115px; }
  .stat-value {
    font-family: "Rajdhani", sans-serif; font-weight: 300; font-size: 37px;
    line-height: 1; color: var(--accent);
  }
  .stat-label {
    margin-top: 7px; font-family: "Rajdhani", sans-serif; font-weight: 400;
    font-size: 16px; letter-spacing: 0.3px; line-height: 1.2;
  }
  .stat-text {
    margin-top: 8px; font-size: 10px; line-height: 15.5px; letter-spacing: 0.3px; color: var(--muted);
  }
  .quote-mark { position: absolute; top: 445px; left: 582px; }
</style>
</head>
<body>
  <header class="site-header">
    <a class="nav-link" style="left:200px" href="#">Home</a>
    <a class="nav-link" style="left:246px" href="#">Advisory Services</a>
    <a class="nav-link" style="left:343px" href="#">About Us</a>
    <div class="brand"><span class="brand-dot"></span>Harrowfield Bright Associates</div>
    <a class="nav-link" style="left:938px" href="#">Blog</a>
    <a class="nav-link" style="left:978px" href="#">Contact Us</a>
  </header>

  <section class="results">
    <h1 class="results-title">Proven Results That Drive Real Growth</h1>
    <p class="results-intro">We've helped brands strengthen their digital presence, expand their network, and accelerate opportunities across the defense, space, and government sectors.</p>

    <div class="stat" style="left:355px">
      <div class="stat-value">+72%</div>
      <div class="stat-label">Database Growth</div>
      <p class="stat-text">Through CRM implementation and targeted marketing</p>
    </div>
    <div class="stat" style="left:614px">
      <div class="stat-value">100+</div>
      <div class="stat-label">Strategic Introductions</div>
      <p class="stat-text">Tech-scouting contracts across DoD and aerospace</p>
    </div>
    <div class="stat" style="left:872px">
      <div class="stat-value">570%</div>
      <div class="stat-label">Stock Growth</div>
      <p class="stat-text">Positioned client for transformative growth with $50M AUD investment</p>
    </div>

    <svg class="quote-mark" width="36" height="36" viewBox="0 0 36 36" aria-hidden="true">
      <g fill="none" stroke="var(--quote)" stroke-width="2.6" stroke-linejoin="round">
        <path d="M3 3h11v14c0 8-4 13-11 16v-5c4-2 5-5 5-8H3z"/>
        <path d="M21 3h11v14c0 8-4 13-11 16v-5c4-2 5-5 5-8h-5z"/>
      </g>
    </svg>
  </section>
</body>
</html>
```